Business Card Design

I need a business card design for my law office based in Pasadena, California. I am a sole practitioner and I specialize in business transaction and litigation, probate and estate planning, taxation law, corporate and business formation, immigration and real estate. I want something that is simple, yet stands out.

A friend helped to create a logo about 6 years ago. I am open to new ideas to changing the logo.

Industry/Entity Type

Business

Contact Information for Business Card

Law Offices of Doran M. Vaske
482 W. Harlow Ave., Suite 312
Pasadena, CA 91108
Tel: 626-503-7719
Fax: 626-581-9046
Email: dvaske@dmvlegalgrp.example

Attorney: Doran M. Vaske

```html
<!DOCTYPE html>
<html lang="en">
<head>
<meta charset="utf-8">
<title>Business Cards – Law Offices of Doran M. Vaske</title>
<link rel="stylesheet" href="https://fonts.googleapis.com/css2?family=Arimo:wght@400;700&display=swap">
<style>
  :root {
    --backdrop: #e8e8ea;
    --card: #efefef;
    --frame: #7a7a7a;
    --ink: #1e1e1e;
    --ink-soft: #2c2c2c;
  }
  * { margin: 0; padding: 0; box-sizing: border-box; }
  html, body {
    width: 1200px; height: 516px; overflow: hidden;
    background: var(--backdrop);
    font-family: "Arimo", Arial, sans-serif;
    color: var(--ink);
  }
  .stage { position: relative; width: 1200px; height: 516px; }

  .card {
    position: absolute; top: 105px;
    width: 524px; height: 323px;
    background: var(--card);
  }
  .card--front { left: 25px; }
  .card--back { left: 642px; }
  .card__frame {
    position: absolute; inset: 8px;
    border: 1px solid var(--frame);
  }

  /* name block standing where the firm mark sits */
  .firm-name {
    position: absolute;
    display: flex; align-items: center; gap: 8px;
    font-weight: 400; color: var(--ink);
  }
  .firm-name__square { background: var(--ink); flex: none; }
  .firm-name__text { line-height: 1.15; }
  .firm-name__pre { display: block; text-transform: uppercase; letter-spacing: 0.3em; }
  .firm-name__main { display: block; text-transform: uppercase; letter-spacing: 0.04em; }

  .card--front .firm-name { left: 40px; top: 46px; }
  .card--front .firm-name__square { width: 14px; height: 14px; }
  .card--front .firm-name__pre { font-size: 6px; }
  .card--front .firm-name__main { font-size: 15px; }

  .card--back .firm-name { right: 44px; bottom: 32px; }
  .card--back .firm-name__square { width: 18px; height: 18px; }
  .card--back .firm-name__pre { font-size: 8px; text-align: right; }
  .card--back .firm-name__main { font-size: 26px; }

  /* contact block */
  .contact { position: absolute; left: 288px; top: 116px; }
  .contact__name {
    display: inline-block;
    font-size: 14px; font-weight: 700;
    padding-bottom: 2px;
    border-bottom: 1px solid var(--ink);
  }
  .contact__address {
    font-style: normal; font-size: 12.5px; line-height: 13px;
    color: var(--ink-soft); margin-top: 5px;
  }
  .contact__lines { list-style: none; margin-top: 11px; margin-left: 22px; }
  .contact__line {
    display: flex; align-items: center; gap: 10px;
    font-size: 12px; font-weight: 700; height: 17px;
  }
  .contact__icon { width: 14px; height: 14px; flex: none; display: flex; align-items: center; justify-content: center; }
  .contact__icon--at { font-size: 13px; font-weight: 700; }
</style>
</head>
<body>
<main class="stage">

  <section class="card card--front" aria-label="Business card front">
    <div class="card__frame"></div>

    <div class="firm-name">
      <span class="firm-name__square"></span>
      <span class="firm-name__text">
        <span class="firm-name__pre">Law Offices of</span>
        <span class="firm-name__main">Doran M. Vaske</span>
      </span>
    </div>

    <div class="contact">
      <p class="contact__name">Attorney Doran M. Vaske</p>
      <address class="contact__address">
        482 W. Harlow Ave.<br>
        Suite 312<br>
        Pasadena<br>
        CA 91108
      </address>
      <ul class="contact__lines">
        <li class="contact__line">
          <span class="contact__icon" aria-label="Telephone">
            <svg viewBox="0 0 24 24" width="13" height="13"><path fill="#1e1e1e" d="M6.6 10.8c1.4 2.8 3.8 5.1 6.6 6.6l2.2-2.2c.3-.3.7-.4 1-.2 1.1.4 2.3.6 3.6.6.6 0 1 .4 1 1V20c0 .6-.4 1-1 1C10.6 21 3 13.4 3 4c0-.6.4-1 1-1h3.5c.6 0 1 .4 1 1 0 1.3.2 2.5.6 3.6.1.3 0 .7-.2 1L6.6 10.8z"/></svg>
          </span>
          <span>626 503 7719</span>
        </li>
        <li class="contact__line">
          <span class="contact__icon" aria-label="Fax">
            <svg viewBox="0 0 24 24" width="14" height="14"><path fill="#1e1e1e" d="M6 2h12v5H6zM3 8h18c1.1 0 2 .9 2 2v7h-4v5H5v-5H1v-7c0-1.1.9-2 2-2zm4 8v4h10v-4H7z"/></svg>
          </span>
          <span>626 581 9046</span>
        </li>
        <li class="contact__line">
          <span class="contact__icon contact__icon--at" aria-label="Email">@</span>
          <span>dvaske@dmvlegalgrp.example</span>
        </li>
      </ul>
    </div>
  </section>

  <section class="card card--back" aria-label="Business card back">
    <div class="card__frame"></div>
    <div class="firm-name">
      <span class="firm-name__square"></span>
      <span class="firm-name__text">
        <span class="firm-name__pre">Law Offices of</span>
        <span class="firm-name__main">Doran M. Vaske</span>
      </span>
    </div>
  </section>

</main>
</body>
</html>
```